I need a new business card design for my pharmacy.

I need a business card design. I will include my logo.
The card needs to be readable. I prefer to have my logo on one side along with my website, the other side includes the other information. Please use combination of black, neon green, white, and silver. This needs to catch the eye but yet be clearly visible and legible. Thanks

Industry/Entity Type

Pharmacy

Contact Information for Business Card

It needs to have the following information listed:
Mel's Apothecary Owner/Pharm D.
7134 North Brook Lane
Sioux Falls, SD 57231
Phone 605-318-6207
Fax 605-318-6209
email: mel@melsapothecary-example.com
www.melsapothecary-example.com
Store hours Monday-Friday 8 am- 7 pm
Saturday 8 am- 12 pm
Sunday Closed
Please utilize the colors black, white, and neon green, maybe silver.

Requirements
Must have
• It needs to be easily readable!
Nice to have
• It should catch the eye.
Should not have
• Do not use any other colors except listed: black, neon green, white, & silver.

```html
<!DOCTYPE html>
<html lang="en">
<head>
<meta charset="utf-8">
<title>Mel's Apothecary – Business Card</title>
<link rel="stylesheet" href="https://fonts.googleapis.com/css2?family=Open+Sans:wght@400;600&display=swap">
<style>
  :root {
    --green: #a6ce39;
    --silver: #7a7b7b;
    --ink: #111111;
    --paper: #ffffff;
    --edge: #3a3a3a;
  }
  * { margin: 0; padding: 0; box-sizing: border-box; }
  html, body { width: 1200px; height: 605px; overflow: hidden; background: var(--paper); }
  body { position: relative; font-family: "Open Sans", Arial, sans-serif; color: var(--ink); }

  .card {
    position: absolute;
    top: 137px;
    width: 483px;
    height: 276px;
    border: 1px solid var(--edge);
    background: var(--paper);
    overflow: hidden;
  }
  .card--front { left: 85px; }
  .card--back { left: 633px; }

  .brand { position: absolute; display: flex; align-items: center; }
  .brand__dot { border-radius: 50%; background: var(--green); flex: none; }
  .brand__divider { width: 2px; background: var(--ink); flex: none; }
  .brand__name { font-weight: 600; letter-spacing: -1px; white-space: nowrap; color: var(--ink); }

  /* Front */
  .card--front .brand { left: 44px; top: 73px; height: 78px; }
  .card--front .brand__dot { width: 46px; height: 46px; margin-right: 22px; }
  .card--front .brand__divider { height: 78px; margin-right: 16px; }
  .card--front .brand__name { font-size: 33px; }

  .front__stripe { position: absolute; left: 0; top: 177px; width: 100%; height: 6px; background: var(--green); }
  .front__band {
    position: absolute; left: 0; top: 183px; width: 100%; height: 93px;
    background: var(--silver); text-align: center;
  }
  .front__web { margin-top: 17px; color: var(--paper); font-size: 21px; letter-spacing: 2.6px; font-weight: 400; }
  .front__hours { margin-top: 6px; font-size: 12.5px; color: var(--ink); }
  .sep { display: inline-block; width: 4px; height: 4px; border-radius: 50%; background: var(--green); vertical-align: middle; margin: 0 5px; }

  /* Back */
  .card--back .brand { left: 24px; top: 16px; height: 48px; }
  .card--back .brand__dot { width: 32px; height: 32px; margin-right: 40px; }
  .card--back .brand__divider { height: 48px; margin-right: 12px; }
  .card--back .brand__name { font-size: 22px; letter-spacing: -0.6px; }

  .back__shape { position: absolute; left: 0; top: 0; }

  .contact { position: absolute; right: 82px; color: var(--paper); font-size: 15px; text-align: right; white-space: nowrap; line-height: 22px; }
  .contact--address { top: 130px; }
  .contact--phones { top: 197px; }
  .contact .sep { width: 3px; height: 3px; margin: 0 3px; }

  .icon { position: absolute; left: 410px; width: 16px; height: 16px; }
  .icon--pin { top: 137px; height: 22px; }
  .icon--phone { top: 200px; }
  .icon--fax { top: 222px; }
  .icon--mail { top: 245px; }
</style>
</head>
<body>

<section class="card card--front" aria-label="Front of business card">
  <div class="brand">
    <span class="brand__dot"></span>
    <span class="brand__divider"></span>
    <span class="brand__name">Mel's Apothecary</span>
  </div>
  <div class="front__stripe"></div>
  <div class="front__band">
    <p class="front__web">www.melsapothecary-example.com</p>
    <p class="front__hours">Monday-Friday 8 am- 7 pm<span class="sep"></span>Saturday 8 am- 12 pm<span class="sep"></span>Sunday Closed</p>
  </div>
</section>

<section class="card card--back" aria-label="Back of business card">
  <div class="brand">
    <span class="brand__dot"></span>
    <span class="brand__divider"></span>
    <span class="brand__name">Mel's Apothecary</span>
  </div>

  <svg class="back__shape" width="483" height="276" viewBox="0 0 483 276" aria-hidden="true">
    <polygon points="9,127 464,58 464,276 443,276 443,70 0,132" fill="var(--green)"/>
    <polygon points="0,132 443,70 443,276 0,276" fill="var(--silver)"/>
  </svg>

  <div class="contact contact--address">
    <p>7134 North Brook Lane</p>
    <p>Sioux Falls, SD 57231</p>
  </div>
  <div class="contact contact--phones">
    <p>605<span class="sep"></span>318<span class="sep"></span>6207</p>
    <p>605<span class="sep"></span>318<span class="sep"></span>6209</p>
    <p>mel@melsapothecary-example.com</p>
  </div>

  <svg class="icon icon--pin" viewBox="0 0 16 22" aria-hidden="true">
    <path d="M8 1a6.5 6.5 0 0 0-6.5 6.5C1.5 12.5 8 20 8 20s6.5-7.5 6.5-12.5A6.5 6.5 0 0 0 8 1z" fill="none" stroke="var(--green)" stroke-width="1.3"/>
    <circle cx="8" cy="7.5" r="2.3" fill="none" stroke="var(--green)" stroke-width="1.3"/>
  </svg>
  <svg class="icon icon--phone" viewBox="0 0 16 16" aria-hidden="true">
    <rect x="4" y="1" width="8" height="14" rx="1.2" fill="none" stroke="var(--green)" stroke-width="1.2"/>
    <rect x="5.8" y="3" width="4.4" height="4" fill="none" stroke="var(--green)" stroke-width="1"/>
    <circle cx="8" cy="12" r="0.9" fill="var(--green)"/>
  </svg>
  <svg class="icon icon--fax" viewBox="0 0 16 16" aria-hidden="true">
    <rect x="1.5" y="7" width="13" height="7" rx="1" fill="none" stroke="var(--green)" stroke-width="1.2"/>
    <path d="M4.5 7V2h7v5" fill="none" stroke="var(--green)" stroke-width="1.2"/>
    <line x1="4" y1="11" x2="12" y2="11" stroke="var(--green)" stroke-width="1"/>
  </svg>
  <svg class="icon icon--mail" viewBox="0 0 16 16" aria-hidden="true">
    <rect x="1" y="3.5" width="14" height="9" fill="none" stroke="var(--green)" stroke-width="1.2"/>
    <path d="M1 3.5l7 5.5 7-5.5" fill="none" stroke="var(--green)" stroke-width="1.2"/>
  </svg>
</section>

</body>
</html>
```